Health Company needs new labels for a new line of natural vitamins and supplements

We are a dutch based health company. We need labels for a new line of healthy, all natural, vitamins and supplements line.
We came across this brand: http://www.velmora.eu , we like that style so you can use this as inspiration.
Key words : Natural , Organic logo's , clear , earthy colors , open , trustworthy , healthy
The product should be leading, the logo/brandname can be small, even only mentioned on the rear label.

Target Market(s)

Health conscious people

Industry/Entity Type

Health And Wellness

Requirements
Must have
• A clear , simple, trustworthy , organic style

```html
<!DOCTYPE html>
<html lang="en">
<head>
<meta charset="utf-8">
<title>Velmora – Natural Vitamin Label</title>
<link href="https://fonts.googleapis.com/css2?family=Montserrat:wght@500;700&display=swap" rel="stylesheet">
<style>
  :root {
    --backdrop: #f2f2f2;
    --label-white: #ffffff;
    --band-orange: #ef5a2f;
    --band-brown: #4a2c1a;
    --band-brown-dark: #351d10;
    --band-green: #4aa614;
    --text-light: #f4f1ec;
    --fruit-peach: #f7c7a0;
    --fruit-orange: #f6a43a;
    --fruit-yellow: #f4d25a;
    --fruit-lime: #d7e98a;
    --fruit-pink: #f3a7a0;
  }
  * { margin: 0; padding: 0; box-sizing: border-box; }
  html, body {
    width: 1056px;
    height: 1200px;
    overflow: hidden;
    background: var(--backdrop);
  }
  .label {
    position: absolute;
    left: 88px;
    top: 80px;
    width: 880px;
    height: 1041px;
    background: var(--label-white);
    font-family: "Montserrat", sans-serif;
  }
  .fruit-panel { position: absolute; }
  .fruit-panel--top-left {
    left: 0; top: 0; width: 341px; height: 407px;
    background: linear-gradient(160deg, var(--fruit-pink) 0%, var(--fruit-peach) 40%, var(--fruit-yellow) 100%);
  }
  .fruit-panel--top-right {
    left: 528px; top: 0; width: 352px; height: 407px;
    background: linear-gradient(200deg, var(--fruit-orange) 0%, var(--fruit-yellow) 45%, var(--fruit-lime) 100%);
  }
  .fruit-panel--bottom-left {
    left: 0; top: 601px; width: 341px; height: 316px;
    background: linear-gradient(20deg, var(--fruit-peach) 0%, var(--fruit-yellow) 55%, var(--fruit-lime) 100%);
  }
  .fruit-panel--bottom-right {
    left: 528px; top: 601px; width: 352px; height: 316px;
    background: linear-gradient(340deg, var(--fruit-orange) 0%, var(--fruit-yellow) 50%, var(--fruit-lime) 100%);
  }
  .band-vertical {
    position: absolute;
    left: 352px; top: 0; width: 161px; height: 917px;
    background: var(--band-orange);
  }
  .brand-mark {
    position: absolute;
    left: 50%; top: 308px;
    width: 46px; height: 46px;
    margin-left: -23px;
    border-radius: 50%;
    background: var(--label-white);
  }
  .band-brand {
    position: absolute;
    left: 0; top: 425px; width: 880px; height: 158px;
    background: linear-gradient(90deg, var(--band-brown) 0%, var(--band-brown) 70%, var(--band-brown-dark) 100%);
    display: flex;
    align-items: center;
    justify-content: center;
  }
  .brand-name {
    color: var(--text-light);
    font-weight: 500;
    font-size: 80px;
    letter-spacing: 10px;
    line-height: 1;
  }
  .band-claim {
    position: absolute;
    left: 0; top: 917px; width: 880px; height: 124px;
    background: var(--band-green);
    display: flex;
    align-items: center;
    justify-content: center;
  }
  .claim-text {
    color: var(--text-light);
    font-weight: 700;
    font-size: 84px;
    letter-spacing: -1px;
    line-height: 1;
  }
</style>
</head>
<body>
  <main class="label">
    <div class="fruit-panel fruit-panel--top-left" role="img" aria-label="Photo of sliced citrus fruits and berries"></div>
    <div class="fruit-panel fruit-panel--top-right" role="img" aria-label="Photo of sliced oranges, limes and tomatoes"></div>
    <div class="fruit-panel fruit-panel--bottom-left" role="img" aria-label="Photo of sliced lemons and strawberries"></div>
    <div class="fruit-panel fruit-panel--bottom-right" role="img" aria-label="Photo of sliced oranges and peppers"></div>

    <div class="band-vertical">
      <span class="brand-mark"></span>
    </div>

    <div class="band-brand">
      <span class="brand-name">VELMORA</span>
    </div>

    <div class="band-claim">
      <span class="claim-text">NATURAL VITAMIN</span>
    </div>
  </main>
</body>
</html>
```